Basic Web Redesign

Hello,

We are working with a client who would like their existing website updated.

The site is http://www.marlowepike.com/

Currently the website is Joomla 1.0.x with Virtuemart running the small online shop.

We are extremely flexible with regards to the way forward - i.e. it can be Joomla 2.5 with Virtuemart, Wordpress plus a shopping cart, HTML 5 (no CMS) with a shopping cart or a full blown ecommerce solution using Prestashop, Magento etc.

The main constraint is a website that incorporates a working shop. At this moment the current website works, but is on extremely old versions of Joomla and Virtuemart.

So the brief is to either migrate the existing offering to a newer version of Joomla and Virtuemart OR use alternative products to achieve a very basic website with shopping cart functionality.

Reason: To enable designer to upload files and installation to be tested.

Target Market(s)

Predominantly people living on the Costa Blanca in Spain, but also some customers in the UK.

Industry/Entity Type

Shop

Requirements
Must have
• Online shop
Shipping calculator
PayPal for accepting payments
Nice to have
• Easy to use front-end for editing shop items
Easy to use front-end for editing non-shop pages

```html
<!DOCTYPE html>
<html lang="en">
<head>
<meta charset="utf-8">
<title>Marlowe Pike Floral Designer</title>
<link rel="stylesheet" href="https://fonts.googleapis.com/css2?family=Cinzel:wght@600&family=Fenix&family=Open+Sans:ital,wght@0,300;0,400;0,600;1,400&display=swap">
<style>
:root{
  --pink:#d2186f;
  --pink-dark:#b9105e;
  --rose:#c7245f;
  --nav:#1f1f1f;
  --text:#555;
  --muted:#777;
  --green:#5aa11a;
  --green-light:#7cc32a;
  --price:#5f9a1c;
  --footer:#2b2b2b;
  --white:#fff;
}
*{box-sizing:border-box;margin:0;padding:0}
html,body{width:874px;height:1200px;overflow:hidden}
body{position:relative;background:var(--white);font-family:"Open Sans",sans-serif;color:var(--text)}
.header-band{position:absolute;left:0;top:0;width:874px;height:296px;background:linear-gradient(#c8106a,var(--pink) 40%,#d41a72)}
.util-links{position:absolute;left:527px;top:6px;width:306px;height:34px;background:var(--pink-dark);border-radius:0 0 6px 6px;display:flex;justify-content:center;align-items:center;gap:7px;color:var(--white);font-size:12px}
.brand{position:absolute;left:36px;top:52px;display:flex;align-items:center;gap:8px;color:var(--white);font-family:"Fenix",serif;font-size:27px}
.brand-mark{width:22px;height:22px;background:var(--white)}
.cart{position:absolute;right:48px;top:74px;color:var(--white);font-size:13px;display:flex;align-items:center;gap:4px}
.cart b{font-size:16px;font-weight:600}
.search{position:absolute;left:623px;top:109px;width:210px;height:25px;background:var(--white);border-radius:2px;font-size:9.5px;font-style:italic;color:#888;padding:6px 10px}
.search svg{position:absolute;right:8px;top:5px}
.main-nav{position:absolute;left:34px;top:147px;width:805px;height:47px;background:linear-gradient(#3a3a3a,var(--nav));border-radius:3px 3px 0 0;display:flex;padding-left:48px}
.main-nav a{color:var(--white);text-decoration:none;font-family:"Cinzel",serif;font-size:14.5px;letter-spacing:1px;padding:0 17px;line-height:47px;border-left:1px solid #555}
.main-nav a:first-child{border-left:none}
.slider{position:absolute;left:35px;top:194px;width:803px;height:294px;background:var(--white);box-shadow:0 2px 6px rgba(0,0,0,.2)}
.slide{position:absolute;left:7px;top:8px;width:790px;height:277px;background:radial-gradient(ellipse at 62% 50%,#f6c2b0 0,#f0a890 22%,#8a70c8 50%,#5d48b0 100%)}
.dots{position:absolute;left:380px;top:264px;display:flex;gap:3px}
.dots i{width:9px;height:9px;border-radius:50%;background:rgba(255,255,255,.7)}
.dots i:first-child{background:var(--white)}
.product{position:absolute;top:512px;width:192px}
.product-photo{width:192px;height:107px}
.product h3{font-family:"Fenix",serif;font-weight:400;color:var(--rose);font-size:18px;margin-top:9px}
.product p{font-size:10px;font-weight:300;line-height:16px;margin-top:1px;color:var(--muted)}
.buy{display:flex;align-items:center;gap:8px;margin-top:5px}
.price{color:var(--price);font-size:19px;font-weight:300}
.add{background:linear-gradient(var(--green-light),var(--green));color:var(--white);font-size:10.5px;border-radius:3px;width:75px;height:25px;line-height:25px;text-align:center}
.divider{position:absolute;left:35px;top:775px;width:803px;height:1px;background:#e4e4e4}
.welcome{position:absolute;left:38px;top:808px;width:545px;z-index:2}
.welcome h1{font-family:"Fenix",serif;font-weight:400;font-size:22px;line-height:28px;color:#444}
.welcome .lead{font-size:11.4px;line-height:17px;margin-top:6px;font-weight:300;color:#444}
.welcome p{font-size:9.8px;line-height:17.2px;margin-top:8px;font-weight:300;color:#444}
.welcome p.more{margin-top:4px}
.testimonials{position:absolute;left:602px;top:808px;width:245px;z-index:2}
.testimonials h2{font-family:"Fenix",serif;font-weight:400;color:var(--rose);font-size:19px}
.quote-mark{position:absolute;left:-4px;top:30px;font-family:"Fenix",serif;font-size:28px;color:#666}
.portrait{position:absolute;left:20px;top:38px;width:66px;height:60px;border:1px solid #ddd;background:linear-gradient(#eef0f2,#c9cfd6)}
.t-side{position:absolute;left:96px;top:36px;width:150px;font-size:9px;font-style:italic;line-height:16px;color:#666}
.t-body{position:absolute;left:18px;top:101px;width:228px;font-size:9px;font-style:italic;line-height:16px;color:#666}
.t-author{position:absolute;left:19px;top:155px;font-size:9.5px;font-weight:600;color:#444}
.tulips{position:absolute;left:0;top:984px;width:874px;height:118px;z-index:1;background:linear-gradient(#fff 0,rgba(255,255,255,0) 45%),linear-gradient(90deg,#e85a94 0,#f3b7c4 30%,#fbeee8 50%,#f6c68f 75%,#f08a1c 100%)}
.footer{position:absolute;left:0;top:1102px;width:874px;height:98px;background:var(--footer)}
.footer-links{position:absolute;left:39px;top:28px;color:var(--white);font-size:12px;display:flex;gap:6px}
.copyright{position:absolute;left:39px;top:52px;color:#888;font-size:10px}
.social{position:absolute;left:750px;top:24px;display:flex;gap:4px}
.social span{width:25px;height:25px;border-radius:3px;background:linear-gradient(#5aa6e8,#2f70c0)}
</style>
</head>
<body>
<div class="header-band"></div>
<nav class="util-links"><span>Map of Delivery</span>|<span>Contact Us</span>|<span>Partners</span>|<span>Links</span></nav>
<div class="brand"><span class="brand-mark"></span>Marlowe Pike</div>
<div class="cart">
<svg width="26" height="24" viewBox="0 0 26 24" fill="none" stroke="#fff" stroke-width="2"><path d="M1 2h4l3 13h13l3-9H7"/><circle cx="10" cy="20" r="2"/><circle cx="19" cy="20" r="2"/></svg>
My Cart <b>0 itmes</b></div>
<div class="search">Search here..
<svg width="15" height="15" viewBox="0 0 15 15" fill="none" stroke="#aaa" stroke-width="2"><circle cx="6" cy="6" r="4.5"/><path d="M9.5 9.5l4 4"/></svg></div>
<nav class="main-nav"><a>Home</a><a>About Us</a><a>Flowers for Delivery</a><a>Gifts &amp; Ideas</a><a>Photo Gallery</a></nav>
<div class="slider"><div class="slide" role="img" aria-label="Bunch of peach flowers against blurred violet blooms"></div><div class="dots"><i></i><i></i><i></i><i></i></div></div>

<div class="product" style="left:36px"><div class="product-photo" role="img" aria-label="Pink and white daisies under blue sky" style="background:linear-gradient(#4a8fd8,#e05fa8 60%,#3e7a2a)"></div><h3>Flower Name</h3><p>Nunc tempus felis vitae urna. Vivamus porttitor purus nisi eleifend libero, a tempus libero lectus feugiat</p><div class="buy"><span class="price">$15.00</span><span class="add">Add to Cart</span></div></div>
<div class="product" style="left:240px"><div class="product-photo" role="img" aria-label="Soft purple bellflowers" style="background:linear-gradient(135deg,#c7a3ec,#9a76d6 50%,#f0d8f4)"></div><h3>Flower Name</h3><p>Nunc tempus felis vitae urna. Vivamus porttitor purus nisi eleifend libero, a tempus libero lectus feugiat</p><div class="buy"><span class="price">$15.00</span><span class="add">Add to Cart</span></div></div>
<div class="product" style="left:444px"><div class="product-photo" role="img" aria-label="Red cosmos flowers in a meadow" style="background:linear-gradient(#f4efe4,#e8a0a0 60%,#7a3a30)"></div><h3>Flower Name</h3><p>Nunc tempus felis vitae urna. Vivamus porttitor purus nisi eleifend libero, a tempus libero lectus feugiat</p><div class="buy"><span class="price">$15.00</span><span class="add">Add to Cart</span></div></div>
<div class="product" style="left:648px"><div class="product-photo" role="img" aria-label="Field of white daisies" style="background:linear-gradient(#d8e8b8,#8aa84a 50%,#4d6e22)"></div><h3>Flower Name</h3><p>Nunc tempus felis vitae urna. Vivamus porttitor purus nisi eleifend libero, a tempus libero lectus feugiat</p><div class="buy"><span class="price">$15.00</span><span class="add">Add to Cart</span></div></div>

<div class="divider"></div>
<section class="welcome">
<h1>Welcome to Marlowe Pike Designs Mainpage..</h1>
<p class="lead">We offer beautiful flowers and plants for all tastes and budgets, and whats more, we will deliver them to your loved ones, a service that is not often found in this area of the Costa Blanca, Spain.</p>
<p>We offer a wide selection of bouquets, flower arrangements and plants, all of which are gift wrapped. Our flowers are of the finest quality and are supplied direct from Holland.</p>
<p class="more">However, should you wish to design your own bouquet, perhaps you love a particular flower, or maybe it has a special meaning, then click on 'design own' in the 'Flowers For Delivery' section, and let your imagination run away with you. Perhaps you would like to send a plant or a tree as a birthday gift or as a house warming present, check out our 'Gifts &amp; Ideas' section and take a look at the Lemon tree, delivered with a bottle of Gin and Tonic!</p>
</section>
<aside class="testimonials">
<h2>Testimonials</h2>
<span class="quote-mark">&ldquo;</span>
<div class="portrait" role="img" aria-label="Portrait of a smiling customer"></div>
<p class="t-side">Nunc tempus felis vitae urna. Vivamus porttitor, neque at volut-pat rutrum, purus nisi eleifend libero, a tempus libero lectus</p>
<p class="t-body">Morbi eget arcu. Morbi porta, libero id ullamcorper non-ummy, nibh ligula pulvinar metus, eget consectetuer augue nisi quis lacus. Ut ac mi quis lacus. &rdquo;</p>
<p class="t-author">By Author Name</p>
</aside>
<div class="tulips" role="img" aria-label="Row of pink, peach and orange tulips"></div>
<footer class="footer">
<nav class="footer-links"><span>Home</span>|<span>About Us</span>|<span>Flowers for Delivery</span>|<span>Gifts &amp; Ideas</span>|<span>Photo Gallery</span>|<span>Partners</span>|<span>Contact</span></nav>
<p class="copyright">© 2013 Company Name.&nbsp; All right reserved.&nbsp; Term of Use</p>
<div class="social" aria-label="Social links"><span></span><span></span><span></span></div>
</footer>
</body>
</html>
```